Advertising Material / Stats - InfoGraphic !

We are in the process of charging for people to use the advertising space on our website.

We have all the information and need it put to a great looking format that will catch the clients eye, we are thinking maybe a Infographic

We need our info put into a marketing package ( Image format - pdf ) for clients to use and see our information.

Looking for a smart, eye catching layout. Maybe along the lines of a info-graphic or something like that. We would like out own website colours used. Please visit our website www.platelistly.com.au our colours are black and Green. You can download the logo from our site its a PNG, however it will need to be placed on a black background. Please note : we don't mind images but no corny chef cartoons. This needs to be a Very high Standard and professional as it will be passed out to clients. If the designer works out we will be needing more work done in the future for our other websites.

We have all the relevant info and stats in a document, we just need it turned into package.
Updates

Please make sure the stats part really stands out as this is something a new client will be looking at. 

Would be great to use a graphic that shows how many pages adverts will display on, saying something like - with over 1500 users your advert will display on 6000 plus pages. 

The designs we are seeing so far are not jumping out at us yet, We are really looking for someone to impress us, we want something that our clients will go WOW, think out of the box. All we are seeing so far is coping and pasting from our document. We would like to see some imagination and skills here. 

Industry/Entity Type

Advertising

Requirements
Must have
• Stunning Graphics
InfoGraphics - Or we are open to other ideas
Should not have
• Corny Chef Cartoons. Must be Stunning Graphics

```html
<!DOCTYPE html>
<html lang="en">
<head>
<meta charset="utf-8">
<title>Platelistly – Advertising Guidelines</title>
<link href="https://fonts.googleapis.com/css2?family=Questrial&display=swap" rel="stylesheet">
<style>
  :root{
    --bg:#000000;
    --ink:#ffffff;
    --muted:#bfbfbf;
    --green:#62b92a;
    --band:#222222;
    --panel-core:#52a81f;
    --panel-edge:#1c4409;
    --label:#5fb52a;
    --label-ink:#0c1d04;
  }
  *{margin:0;padding:0;box-sizing:border-box}
  html,body{width:848px;height:1200px;overflow:hidden;background:var(--bg)}
  body{position:relative;font-family:"Questrial",sans-serif;color:var(--ink)}

  .brand{position:absolute;left:606px;top:62px;display:flex;align-items:center;gap:8px}
  .brand-mark{width:16px;height:16px;background:var(--green)}
  .brand-name{font-size:22px;color:var(--green);letter-spacing:-.3px}

  .guidelines{position:absolute;left:99px;top:134px;width:658px}
  .guidelines h1{font-size:21px;font-weight:400;color:var(--green);text-decoration:underline;text-underline-offset:3px;letter-spacing:.5px;margin-bottom:8px}
  .guidelines p{font-size:16px;line-height:19.6px;letter-spacing:.55px;text-align:justify}

  .band{position:absolute;left:0;top:296px;width:848px;height:31px;background:var(--band)}
  .band h2{position:absolute;top:0;font-size:22px;line-height:28px;font-weight:400;color:var(--green);letter-spacing:.6px}
  .band .public{left:92px}
  .band .member{left:508px}

  .panel,.ad{position:absolute;background:radial-gradient(ellipse at center,var(--panel-core) 45%,var(--panel-edge) 100%)}
  .panel-public{left:104px;top:352px;width:237px;height:374px}
  .panel-member{left:511px;top:352px;width:237px;height:173px}
  .panel-label{position:absolute;left:22px;top:16px;width:191px;height:38px;border-radius:4px;background:var(--label);color:var(--label-ink);font-size:16px;line-height:17px;letter-spacing:.5px;text-align:center;padding-top:2px}
  .panel-member .panel-label{left:26px;top:15px;width:192px;height:39px}

  .ad{width:73px;height:60px;color:var(--label-ink);font-size:10.5px;display:flex;align-items:center;justify-content:center}

  .info{position:absolute;left:99px;font-size:16px;line-height:20px;letter-spacing:.7px}
  .info-both{top:765px}
  .info-note{top:823px;width:600px}

  .stats{position:absolute;left:99px;top:925px;width:650px;height:170px;border-top:1px solid var(--band);border-bottom:1px solid var(--band);display:flex;align-items:center;justify-content:space-between;padding:0 20px}
  .stat{text-align:center;width:200px}
  .stat-figure{font-size:54px;line-height:58px;color:var(--green);letter-spacing:1px}
  .stat-caption{font-size:15px;letter-spacing:.6px;color:var(--ink);margin-top:4px}
  .stats-arrow{width:150px;height:40px}
  .stats-line{position:absolute;left:0;bottom:-30px;width:650px;text-align:center;font-size:14px;letter-spacing:.5px;color:var(--muted)}

  .footer-url{position:absolute;left:55px;top:1159px;font-size:18px;letter-spacing:.6px;color:var(--green)}
</style>
</head>
<body>
  <div class="brand"><span class="brand-mark"></span><span class="brand-name">Platelistly</span></div>

  <section class="guidelines">
    <h1>Advertising Guidelines:</h1>
    <p>Advertisement Images must be in file types: JPG, JPEG and PNG - Max file size: 2MB.Advertisement Images must be : &nbsp;200px by 200px or &nbsp;Width 200 - Height 200.Please include the link that will be added to the image. Example. - &nbsp;http://www.platelistly.com.au</p>
  </section>

  <div class="band">
    <h2 class="public">Public Area Advertising</h2>
    <h2 class="member">Member Area Adverting</h2>
  </div>

  <div class="panel panel-public"><div class="panel-label">Public Area<br>News &amp; Jobs</div></div>
  <div class="ad" style="left:347px;top:352px">Ad-1</div>
  <div class="ad" style="left:347px;top:432px">Ad-2</div>
  <div class="ad" style="left:347px;top:509px">Ad-3</div>
  <div class="ad" style="left:347px;top:588px">Ad-4</div>
  <div class="ad" style="left:347px;top:666px">Ad-5</div>

  <div class="panel panel-member"><div class="panel-label">Members Area<br>Platelistly Content</div></div>
  <div class="ad" style="left:511px;top:531px">Ad-1</div>
  <div class="ad" style="left:594px;top:531px">Ad-2</div>
  <div class="ad" style="left:676px;top:531px">Ad-3</div>

  <p class="info info-both">Your advert will display in both areas</p>
  <p class="info info-note">Note: If you need assistance creating or developing a banner for your advertisement please contact us we are happy to help.</p>

  <section class="stats" aria-label="Audience reach">
    <div class="stat">
      <div class="stat-figure">1500+</div>
      <div class="stat-caption">registered users</div>
    </div>
    <svg class="stats-arrow" viewBox="0 0 150 40" aria-hidden="true">
      <line x1="8" y1="20" x2="132" y2="20" stroke="#62b92a" stroke-width="3"/>
      <polyline points="120,8 138,20 120,32" fill="none" stroke="#62b92a" stroke-width="3"/>
    </svg>
    <div class="stat">
      <div class="stat-figure">6000+</div>
      <div class="stat-caption">pages showing your advert</div>
    </div>
    <p class="stats-line">With over 1500 users your advert will display on 6000 plus pages</p>
  </section>

  <div class="footer-url">www.platelistly.com.au</div>
</body>
</html>
```